Sunreach Youth Ballclub (SYB) Landing Page

We have a very time sensitive project to create a landing page plus 4 carousel pages for SYB. Directions for each page is included in the attached document.
If you have any questions please message immediately as we need to complete this website by the end of the week.

Coded - Design and coding required

1 page

```html
<!DOCTYPE html>
<html lang="en">
<head>
<meta charset="utf-8">
<title>SYB Landing Page and Carousel Slides</title>
<link href="https://fonts.googleapis.com/css2?family=Poppins:ital,wght@0,400;0,500;0,600;0,700;0,800;1,700;1,800&display=swap" rel="stylesheet">
<style>
:root{
  --board:#e4e2de;
  --ink:#2b2b2b;
  --dark:#262626;
  --blue:#2a1fd0;
  --blue-glass:rgba(42,31,208,.86);
  --orange:#f7931e;
  --white:#ffffff;
  --soft:#f2f2f2;
  --muted:#555555;
  --line:#e6e6e6;
}
*{margin:0;padding:0;box-sizing:border-box}
html,body{width:1200px;height:1157px;overflow:hidden}
body{background:var(--board);font-family:"Poppins",sans-serif;color:var(--ink);position:relative}
.panel{position:absolute;background:var(--white);overflow:hidden}
.landing{left:41px;top:34px;width:557px;height:1081px}
.slide{left:614px;width:557px;height:343px}
.slide-1{top:34px}.slide-2{top:403px}.slide-3{top:773px}

.site-header{position:absolute;left:0;top:0;width:100%;height:51px;background:var(--white)}
.site-header .bar{position:absolute;inset:0;background:var(--dark);clip-path:polygon(152px 0,100% 0,100% 100%,118px 100%)}
.brand{position:absolute;left:35px;top:12px;font-weight:800;font-size:22px;letter-spacing:1px;color:var(--blue);line-height:26px}
.nav{position:absolute;right:34px;top:0;height:51px;display:flex;align-items:center;gap:22px}
.nav a,.footer-nav a{color:var(--white);text-decoration:none;font-weight:700;font-style:italic;font-size:7.6px;letter-spacing:.2px}

.hero{position:absolute;left:0;top:51px;width:557px;height:292px}
.photo{position:absolute;inset:0}
.hero-batter{background:linear-gradient(120deg,#1c1a3c 0%,#3a3554 35%,#8a8796 60%,#4a4660 80%,#2a2740 100%)}
.hero-analyst{background:linear-gradient(110deg,#d9dde2 0%,#b9c0c9 35%,#6b6a70 65%,#3b3a3e 100%)}
.hero-security{background:linear-gradient(110deg,#1b1d36 0%,#3c3a56 35%,#a08c78 65%,#c9b6a2 100%)}
.hero-tablet{background:linear-gradient(110deg,#0f4a5c 0%,#2aa3b8 35%,#5f8a5a 65%,#7fa07a 100%)}
.glass{position:absolute;inset:0;background:var(--blue-glass);clip-path:polygon(294px 223px,100% 223px,100% 100%,228px 100%)}
.slide .glass{clip-path:polygon(288px 173px,100% 173px,100% 100%,230px 100%)}
.slide-2 .glass{clip-path:polygon(290px 173px,100% 173px,100% 100%,230px 100%)}
.slide-3 .glass{clip-path:polygon(292px 173px,100% 173px,100% 100%,230px 100%)}
.hero-copy{position:absolute;color:var(--white)}
.hero-title{font-weight:800;font-style:italic;font-size:16px;line-height:18.5px;letter-spacing:.3px;text-transform:uppercase}
.hero-text{font-size:9.6px;line-height:13px;font-weight:500;margin-top:10px}
.ticks{list-style:none;margin-top:8px;font-size:9.6px;font-weight:500;line-height:13px}
.ticks.inline{display:flex;gap:10px}
.ticks li{display:flex;align-items:flex-start;gap:6px;margin-bottom:5px}
.ticks svg{flex:none;margin-top:3px}
.dots{position:absolute;left:35px;bottom:28px;display:flex;gap:5px}
.dots i{width:5px;height:5px;border-radius:50%;background:#111}
.dots i:first-child{background:var(--blue)}

.featured{position:absolute;left:0;top:343px;width:557px;height:172px}
.featured .band{position:absolute;inset:0;background:var(--blue);clip-path:polygon(0 0,228px 0,137px 100%,0 100%)}
.featured h2{position:absolute;left:35px;top:51px;color:var(--white);font-weight:800;font-size:17px;line-height:18.5px;letter-spacing:.3px}
.btn{position:absolute;left:35px;top:132px;width:76px;height:21px;background:var(--orange);color:var(--white);font-weight:700;font-size:7px;display:flex;align-items:center;justify-content:center;text-decoration:none}
.video{position:absolute;top:25px;width:157px}
.video .thumb{position:relative;height:123px}
.video .thumb svg{position:absolute;left:50%;top:50%;transform:translate(-50%,-50%)}
.video h3{margin-top:8px;text-align:center;color:var(--blue);font-size:7.6px;font-weight:600}
.video p{text-align:center;font-size:6.3px;color:var(--muted);margin-top:1px}
.v1{left:134px}.v1 .thumb{background:linear-gradient(160deg,#9fb3c9,#6c7f95 50%,#7f9a6a)}
.v2{left:298px}.v2 .thumb{background:linear-gradient(160deg,#8aa0b8,#3a3f5c 55%,#20253e)}
.v3{left:462px}.v3 .thumb{background:linear-gradient(160deg,#6c7a84,#b9a38a 50%,#5e7a4a)}

.roster{position:absolute;left:0;width:557px}
.alumni{top:547px;height:217px;background:var(--soft)}
.commits{top:764px;height:220px;background:var(--white)}
.roster h2{position:absolute;left:35px;top:27px;font-weight:700;font-size:17px;letter-spacing:.2px;color:var(--ink)}
.arrows{position:absolute;right:35px;top:31px;display:flex;gap:2px}
.arrows span{width:15px;height:14px;display:flex;align-items:center;justify-content:center;background:var(--white);border:1px solid var(--line)}
.arrows span.next{background:var(--blue);border-color:var(--blue)}
.card{position:absolute;width:112px;height:126px;background:var(--white);border:1px solid var(--line);text-align:center}
.alumni .card{top:61px}.commits .card{top:61px}
.card .crest{width:66px;height:66px;border-radius:50%;margin:10px auto 0}
.card h4{margin-top:14px;color:var(--blue);font-size:7.4px;font-weight:700;text-transform:uppercase}
.card p{font-size:5.8px;line-height:9.6px;color:var(--muted);margin-top:2px;padding:0 8px}
.commits .card h4{margin-top:22px}
.c1{left:35px}.c2{left:160px}.c3{left:286px}.c4{left:411px}

.site-footer{position:absolute;left:0;top:984px;width:557px;height:97px;background:var(--dark);color:var(--white)}
.footer-nav{position:absolute;left:35px;top:25px;display:flex;gap:22px}
.copyright{position:absolute;left:35px;top:47px;font-size:6.2px}
.social{position:absolute;left:35px;top:62px;display:flex;gap:10px}
.social i{width:10px;height:10px;border-radius:50%;background:var(--white)}
.powered{position:absolute;left:411px;top:21px;font-size:7px}
.partner{position:absolute;left:411px;top:42px;display:flex;align-items:center;gap:6px;font-size:13px;font-weight:500}
.partner i{width:20px;height:20px;border-radius:50%;border:2px solid var(--white)}
</style>
</head>
<body>

<section class="panel landing" aria-label="SYB landing page">
  <header class="site-header">
    <div class="bar"></div>
    <div class="brand">SYB</div>
    <nav class="nav"><a href="#">REGISTER</a><a href="#">MINT NFTS</a><a href="#">BUY/SELL/TRADE NFTS</a><a href="#">TUTORIALS</a><a href="#">HELP</a></nav>
  </header>
  <div class="hero">
    <div class="photo hero-batter" role="img" aria-label="Photo of a batter and catcher under stadium lights"></div>
    <div class="glass"></div>
    <div class="hero-copy" style="left:300px;top:203px;width:230px">
      <h1 class="hero-title">Sunreach Youth Ballclub</h1>
      <p class="hero-text">The syb family strives to have well rounded players. We feel being talented on the field is just one of the qualities we look for.</p>
    </div>
    <div class="dots" style="left:35px;bottom:28px"><i></i><i></i><i></i><i></i></div>
  </div>

  <section class="featured">
    <div class="band"></div>
    <h2>FEATURED<br>VIDEOS</h2>
    <a class="btn" href="#">SEE ALL VIDEO</a>
    <article class="video v1"><div class="thumb" role="img" aria-label="Video still of a player at batting practice"><svg width="22" height="22" viewBox="0 0 22 22"><circle cx="11" cy="11" r="10" fill="none" stroke="#fff" stroke-width="1.6"/><path d="M8.5 6.5v9l7-4.5z" fill="#fff"/></svg></div><h3>SYB FAMILY</h3><p>December 4, 2020</p></article>
    <article class="video v2"><div class="thumb" role="img" aria-label="Video still of a batter in a helmet"><svg width="22" height="22" viewBox="0 0 22 22"><circle cx="11" cy="11" r="10" fill="none" stroke="#fff" stroke-width="1.6"/><path d="M8.5 6.5v9l7-4.5z" fill="#fff"/></svg></div><h3>SYB FAMILY</h3><p>December 4, 2020</p></article>
    <article class="video v3"><div class="thumb" role="img" aria-label="Video still of a catcher and umpire behind the plate"><svg width="22" height="22" viewBox="0 0 22 22"><circle cx="11" cy="11" r="10" fill="none" stroke="#fff" stroke-width="1.6"/><path d="M8.5 6.5v9l7-4.5z" fill="#fff"/></svg></div><h3>SYB FAMILY</h3><p>December 4, 2020</p></article>
  </section>

  <section class="roster alumni">
    <h2>MAJOR LEAGUE ALUMNI</h2>
    <div class="arrows"><span><svg width="6" height="8"><path d="M5 1L2 4l3 3" fill="none" stroke="#2a1fd0" stroke-width="1.5"/></svg></span><span class="next"><svg width="6" height="8"><path d="M1 1l3 3-3 3" fill="none" stroke="#fff" stroke-width="1.5"/></svg></span></div>
    <div class="card c1"><div class="crest" style="background:#f26b1d"></div><h4>Dane Holloway</h4><p>Harbor Hawks, SYB Chandler &amp; SYB/Redbirds ST</p></div>
    <div class="card c2"><div class="crest" style="background:#1d4fa3"></div><h4>Dane Holloway</h4><p>Harbor Hawks, SYB Chandler &amp; SYB/Redbirds ST</p></div>
    <div class="card c3"><div class="crest" style="background:#2756a5"></div><h4>Dane Holloway</h4><p>Harbor Hawks, SYB Chandler &amp; SYB/Redbirds ST</p></div>
    <div class="card c4"><div class="crest" style="background:#d9252c"></div><h4>Dane Holloway</h4><p>Harbor Hawks, SYB Chandler &amp; SYB/Redbirds ST</p></div>
  </section>

  <section class="roster commits">
    <h2>COLLEGE COMMITS</h2>
    <div class="arrows"><span><svg width="6" height="8"><path d="M5 1L2 4l3 3" fill="none" stroke="#2a1fd0" stroke-width="1.5"/></svg></span><span class="next"><svg width="6" height="8"><path d="M1 1l3 3-3 3" fill="none" stroke="#fff" stroke-width="1.5"/></svg></span></div>
    <div class="card c1"><div class="crest" style="background:#c8102e"></div><h4>Marcus Reyes</h4><p>Riverton</p></div>
    <div class="card c2"><div class="crest" style="background:#1f6f4a"></div><h4>Marcus Reyes</h4><p>Riverton</p></div>
    <div class="card c3"><div class="crest" style="background:#1e6b3a"></div><h4>Marcus Reyes</h4><p>Riverton</p></div>
    <div class="card c4"><div class="crest" style="background:#b8a06a"></div><h4>Marcus Reyes</h4><p>Riverton</p></div>
  </section>

  <footer class="site-footer">
    <nav class="footer-nav"><a href="#">REGISTER</a><a href="#">MINT NFTS</a><a href="#">BUY/SELL/TRADE NFTS</a><a href="#">TUTORIALS</a><a href="#">HELP</a></nav>
    <p class="copyright">Copyright © 2022 Company Name&nbsp; All rights reserved.</p>
    <div class="social" aria-label="Social links"><i></i><i></i><i></i><i></i><i></i></div>
    <p class="powered">Powered by</p>
    <div class="partner"><i></i>Ledgerline</div>
  </footer>
</section>

<section class="panel slide slide-1" aria-label="Carousel slide: document your experience">
  <header class="site-header"><div class="bar"></div><div class="brand">SYB</div><nav class="nav"><a href="#">REGISTER</a><a href="#">MINT NFTS</a><a href="#">BUY/SELL/TRADE NFTS</a><a href="#">TUTORIALS</a><a href="#">HELP</a></nav></header>
  <div class="hero">
    <div class="photo hero-analyst" role="img" aria-label="Photo of a hand marking charts beside a pitcher gripping a ball"></div>
    <div class="glass"></div>
    <div class="hero-copy" style="left:300px;top:193px;width:240px">
      <h2 class="hero-title">Document your SYB experience and manage your data assets</h2>
      <ul class="ticks inline">
        <li><svg width="8" height="7"><path d="M1 3.5l2 2L7 1" fill="none" stroke="#fff" stroke-width="1.6"/></svg>Videos</li>
        <li><svg width="8" height="7"><path d="M1 3.5l2 2L7 1" fill="none" stroke="#fff" stroke-width="1.6"/></svg>Pictures</li>
        <li><svg width="8" height="7"><path d="M1 3.5l2 2L7 1" fill="none" stroke="#fff" stroke-width="1.6"/></svg>Awards</li>
      </ul>
    </div>
    <div class="dots"><i></i><i></i><i></i><i></i></div>
  </div>
</section>

<section class="panel slide slide-2" aria-label="Carousel slide: security and ownership">
  <header class="site-header"><div class="bar"></div><div class="brand">SYB</div><nav class="nav"><a href="#">REGISTER</a><a href="#">MINT NFTS</a><a href="#">BUY/SELL/TRADE NFTS</a><a href="#">TUTORIALS</a><a href="#">HELP</a></nav></header>
  <div class="hero">
    <div class="photo hero-security" role="img" aria-label="Photo of a batter at the plate blended with hands typing and security icons"></div>
    <div class="glass"></div>
    <div class="hero-copy" style="left:319px;top:203px;width:230px">
      <h2 class="hero-title">Security &amp; Ownership</h2>
      <ul class="ticks">
        <li><svg width="8" height="7"><path d="M1 3.5l2 2L7 1" fill="none" stroke="#fff" stroke-width="1.6"/></svg>Own 100% rights to your data</li>
        <li><svg width="8" height="7"><path d="M1 3.5l2 2L7 1" fill="none" stroke="#fff" stroke-width="1.6"/></svg>Keep your data and images secure</li>
      </ul>
    </div>
    <div class="dots"><i></i><i></i><i></i><i></i></div>
  </div>
</section>

<section class="panel slide slide-3" aria-label="Carousel slide: data management habits">
  <header class="site-header"><div class="bar"></div><div class="brand">SYB</div><nav class="nav"><a href="#">REGISTER</a><a href="#">MINT NFTS</a><a href="#">BUY/SELL/TRADE NFTS</a><a href="#">TUTORIALS</a><a href="#">HELP</a></nav></header>
  <div class="hero">
    <div class="photo hero-tablet" role="img" aria-label="Photo of a hand on a glowing tablet beside a batter and catcher on a field"></div>
    <div class="glass"></div>
    <div class="hero-copy" style="left:300px;top:192px;width:240px">
      <h2 class="hero-title">Create data management habits that serve you throughout your career</h2>
      <ul class="ticks">
        <li><svg width="8" height="7"><path d="M1 3.5l2 2L7 1" fill="none" stroke="#fff" stroke-width="1.6"/></svg>Manage and monetize your data<br>and images</li>
      </ul>
    </div>
    <div class="dots"><i></i><i></i><i></i><i></i></div>
  </div>
</section>

</body>
</html>
```